Doctors clinic requires stationary designed

We require various types of stationary to be design based on the logo (attached). We require the following:
- Letterhead (A4 Portrait)
- Business Card (must include UV spot on rear)
- With compliments slip (DL Landscape)
- Appointments card (Folded A6)

We are a young clinical practice which boasts a modern and sophisticated approach to medicine so we require something which feels fresh and modern. Please include colours represented in the logo (contrasting teal and grey). We are calling for creative minds to put forth their ideas and we will be actively providing feedback on all designs.

thank you

```html
<!DOCTYPE html>
<html lang="en">
<head>
<meta charset="utf-8">
<title>Letterhead – Dr Laura Fenwick</title>
<link href="https://fonts.googleapis.com/css2?family=Mulish:wght@400;600;700&display=swap" rel="stylesheet">
<style>
  :root {
    --teal: #1e8f88;
    --grey: #8a8d8f;
    --ink: #4a4d50;
    --paper: #ffffff;
    --backdrop: #e9eaea;
    --rule: #c9cbcc;
  }
  * { margin: 0; padding: 0; box-sizing: border-box; }
  html, body {
    width: 1200px;
    height: 936px;
    overflow: hidden;
    background: var(--backdrop);
    font-family: "Mulish", sans-serif;
  }
  .letterhead {
    position: absolute;
    left: 296px;
    top: 38px;
    width: 608px;
    height: 860px;
    background: var(--paper);
    overflow: hidden;
    box-shadow: 0 2px 10px rgba(0,0,0,0.08);
  }
  .brand {
    position: absolute;
    left: 44px;
    top: 52px;
    display: flex;
    align-items: center;
    gap: 12px;
  }
  .brand-dot {
    width: 34px;
    height: 34px;
    border-radius: 50%;
    border: 2px solid var(--teal);
  }
  .brand-name {
    font-size: 20px;
    font-weight: 700;
    color: var(--teal);
    line-height: 1.1;
    letter-spacing: -0.2px;
  }
  .brand-role {
    font-size: 10.5px;
    font-weight: 700;
    color: var(--teal);
    margin-top: 2px;
  }
  .brand-role .conj {
    font-weight: 400;
    color: var(--grey);
    font-size: 9px;
  }
  .corner-accent {
    position: absolute;
    right: -34px;
    top: 300px;
  }
  .contact {
    position: absolute;
    left: 300px;
    bottom: 44px;
    display: flex;
    align-items: center;
    gap: 16px;
    font-size: 8.5px;
    color: var(--ink);
    line-height: 1.55;
  }
  .contact-divider {
    width: 1px;
    height: 26px;
    background: var(--rule);
  }
  .contact-line {
    display: flex;
    align-items: center;
    gap: 5px;
  }
  .contact-icon { width: 9px; height: 9px; flex: none; }
</style>
</head>
<body>
  <main class="letterhead">
    <header class="brand">
      <span class="brand-dot"></span>
      <div>
        <div class="brand-name">Dr Laura Fenwick</div>
        <div class="brand-role">Obstetrician <span class="conj">and</span> Gynaecologist</div>
      </div>
    </header>

    <svg class="corner-accent" width="110" height="110" viewBox="0 0 110 110" aria-hidden="true">
      <circle cx="55" cy="55" r="50" fill="none" stroke="var(--teal)" stroke-width="4"/>
    </svg>

    <footer class="contact">
      <address class="contact-address" style="font-style:normal">
        42 ORCHARD LANE<br>
        Milford, PA 18337
      </address>
      <span class="contact-divider"></span>
      <div>
        <div class="contact-line">
          <svg class="contact-icon" viewBox="0 0 10 10" aria-hidden="true">
            <circle cx="5" cy="5" r="5" fill="var(--teal)"/>
            <path d="M3.2 2.6c.3-.3.6-.2.8.1l.4.7c.1.2 0 .4-.2.6-.2.2 0 .6.5 1.1.5.5.9.7 1.1.5.2-.2.4-.3.6-.2l.7.4c.3.2.4.5.1.8-.5.6-1.4.5-2.6-.6-1.1-1.1-1.9-2.3-1.4-3.4z" fill="#fff"/>
          </svg>
          (555) 014-2288
        </div>
        <div class="contact-line">
          <svg class="contact-icon" viewBox="0 0 10 10" aria-hidden="true">
            <circle cx="5" cy="5" r="5" fill="var(--teal)"/>
            <rect x="2.4" y="3.2" width="5.2" height="3.6" fill="none" stroke="#fff" stroke-width="0.7"/>
            <path d="M2.4 3.2 5 5.2 7.6 3.2" fill="none" stroke="#fff" stroke-width="0.7"/>
          </svg>
          laura@fenwickclinic.com
        </div>
      </div>
    </footer>
  </main>
</body>
</html>
```